Hack my website! Blue Harbor needs a site

We hack stuff. No joke, that is what we do, but we are the good guys!

We do security consulting, specifically offensive security. The technical term is "Penetration Testing", but you probably know it as "hacking". Companies hire us to break in before the bad guys do. (I have a very cool job :) ).

I need a web site to describe our offerings and connect with clients.

I've included my business card and logo so you can understand what I'm looking for on the website and the color scheme.

Tag line:
Offensive Services from Offensive Minds

Target Market(s)

Medium to large businesses

Industry/Entity Type

Computer Security

Coding

Coded - Design and coding required

Number of Pages Required

2 page

Font styles to use
Sans Serif

Colors

Designer to choose colors to be used in the design.

Requirements
Must have
• Flat, clean, professional look
Nice to have
• Bonus for bootstrap. See the uploaded logo for the current colors. I'd really like this to look decent on a phone too.
Should not have
• 1. Black background
• 2. The business card is to show the colors and theme so far. Please, do NOT just slam that into the middle of the site since it doesn't make sense. It feels odd that I have to say that, but I've received multiple submissions where people have done this.

```html
<!DOCTYPE html>
<html lang="en">
<head>
<meta charset="utf-8">
<title>Blue Harbor — Offensive Services from Offensive Minds</title>
<link href="https://fonts.googleapis.com/css2?family=Lato:ital,wght@0,400;0,700;0,900;1,700&family=Open+Sans:wght@400;600;700&display=swap" rel="stylesheet">
<style>
:root{
  --red:#c8161d;
  --red-dark:#a10f16;
  --ink:#2b2b2b;
  --text:#555;
  --muted:#8a8a8a;
  --line:#e3e3e3;
  --footer:#232323;
  --footer-text:#cfcfcf;
  --white:#fff;
  --star:#f5b301;
}
*{margin:0;padding:0;box-sizing:border-box}
html,body{width:1200px;height:3488px;overflow:hidden}
body{position:relative;background:var(--white);font-family:"Open Sans",Arial,sans-serif;color:var(--text)}
h2.section-title{position:absolute;left:0;width:1200px;text-align:center;font-family:"Lato",Arial,sans-serif;font-weight:700;font-size:30px;color:var(--ink);letter-spacing:.5px}

/* header */
.site-header{position:absolute;top:0;left:0;width:1200px;height:88px;background:var(--white);z-index:3}
.topbar{position:absolute;right:100px;top:14px;font-size:14px;color:var(--ink);display:flex;gap:12px;align-items:center}
.topbar .sep{color:var(--muted)}
.topbar svg{vertical-align:-2px;margin-right:6px}
.main-nav{position:absolute;right:100px;top:54px;display:flex;gap:28px;font-family:"Lato",Arial,sans-serif;font-weight:700;font-size:15px;color:var(--ink);align-items:center}
.main-nav .active{color:var(--red)}
.brand-disc{position:absolute;left:70px;top:-112px;width:274px;height:280px;border-radius:50%;background:var(--white);z-index:4}
.brand{position:absolute;left:70px;top:12px;width:274px;text-align:center;z-index:5}
.brand .mark{width:56px;height:56px;background:var(--red);margin:0 auto 16px}
.brand .name{font-family:"Lato",Arial,sans-serif;font-weight:700;font-size:25px;line-height:30px;letter-spacing:3px;color:var(--ink);white-space:nowrap}

/* hero */
.hero{position:absolute;top:88px;left:0;width:1200px;height:475px;background:linear-gradient(110deg,#1c1f26 0%,#2c3546 40%,#3f5f86 70%,#5a7fa8 100%)}
.hero .tagline-small{position:absolute;left:100px;top:205px;font-family:"Lato",Arial,sans-serif;font-style:italic;font-weight:700;font-size:30px;color:var(--white)}
.hero .tagline-big{position:absolute;left:100px;top:250px;font-family:"Lato",Arial,sans-serif;font-weight:900;font-size:50px;color:var(--white);letter-spacing:1px}
.hero .dots{position:absolute;top:408px;left:0;width:1200px;display:flex;justify-content:center;gap:6px}
.hero .dots span{width:12px;height:12px;border-radius:50%;border:2px solid var(--white)}
.hero .dots span.on{background:var(--white)}

/* welcome */
.welcome-text{position:absolute;top:688px;left:250px;width:700px;text-align:center;font-size:14px;line-height:24px;color:var(--text)}
.feature{position:absolute;top:785px;width:330px;text-align:center}
.feature svg{display:block;margin:0 auto}
.feature h3{margin-top:26px;font-family:"Open Sans",Arial,sans-serif;font-weight:600;font-size:17px;color:var(--ink)}
.feature p{margin:14px auto 0;width:290px;font-size:13.5px;line-height:22px;color:var(--muted)}

/* video */
.video-band{position:absolute;top:1095px;left:0;width:1200px;height:370px;background:linear-gradient(120deg,#cfd4da 0%,#a9b0b8 45%,#7d8590 100%)}
.play{position:absolute;left:566px;top:148px;width:68px;height:68px;border-radius:50%;border:3px solid var(--white)}

/* services */
.service{position:absolute;overflow:hidden}
.service .photo{position:absolute;inset:0}
.service .label{position:absolute;left:0;right:0;bottom:22px;text-align:center;font-family:"Open Sans",Arial,sans-serif;font-weight:600;font-size:16px;line-height:24px;color:var(--white);padding:0 10px}

/* testimonials */
.testimonials{position:absolute;top:2144px;left:0;width:1200px;height:375px;background:linear-gradient(90deg,var(--red-dark),var(--red) 50%,var(--red-dark))}
.testimonials h2.section-title{color:var(--white);top:86px}
.arrow{position:absolute;top:202px;width:34px;height:34px;border-radius:50%;border:1px solid rgba(255,255,255,.6)}
.quote-card{position:absolute;top:172px;width:330px}
.avatar{position:absolute;left:0;top:0;width:72px;height:72px;border-radius:50%;border:3px solid var(--white);background:linear-gradient(160deg,#d9c6b5,#8a7565)}
.quote-card .body{position:absolute;left:90px;top:0;width:240px}
.quote-card .q{font-family:"Lato",Arial,sans-serif;font-style:italic;font-size:12.5px;line-height:20px;color:#f7dede}
.quote-card .q b{font-size:26px;color:var(--white);vertical-align:-8px;margin-right:6px}
.quote-card .who{margin-top:16px;font-size:10.5px;font-weight:700;color:var(--white);text-transform:uppercase}
.quote-card .role{font-size:9.5px;font-style:italic;color:#f2c9c9}
.quote-card .stars{margin-top:8px;font-size:20px;letter-spacing:2px;color:var(--star)}

/* news */
.news{position:absolute;top:2668px;width:323px}
.news .photo{height:183px}
.news h3{margin-top:44px;font-family:"Open Sans",Arial,sans-serif;font-weight:700;font-size:17px;color:var(--ink)}
.news .meta{margin-top:10px;font-size:12px;color:var(--muted);display:flex;gap:8px;align-items:center}
.news .meta .bar{width:1px;height:14px;background:var(--red)}
.news p{margin-top:10px;font-size:12.5px;line-height:20px;color:var(--muted)}
.news .more{margin-top:16px;font-size:12.5px;font-weight:700;color:var(--red)}

/* footer */
.site-footer{position:absolute;top:3109px;left:0;width:1200px;height:379px;background:var(--footer);color:var(--footer-text)}
.footer-brand{position:absolute;left:84px;top:100px;width:280px;text-align:center}
.footer-brand .mark{width:70px;height:70px;background:var(--red);margin:0 auto 22px}
.footer-brand .name{font-family:"Lato",Arial,sans-serif;font-weight:700;font-size:27px;line-height:34px;letter-spacing:3px;color:var(--white);white-space:nowrap}
.footer-col{position:absolute;top:82px}
.footer-col h4{font-family:"Open Sans",Arial,sans-serif;font-weight:600;font-size:17px;color:var(--white);margin-bottom:30px}
.footer-col li{list-style:none;font-size:12.5px;line-height:29px;color:var(--footer-text)}
.footer-col p{font-size:12.5px;line-height:20px}
.news-input{margin-top:18px;width:255px;height:34px;background:var(--white)}
.subscribe{margin-top:14px;display:inline-block;padding:7px 18px;border-radius:20px;background:var(--red);color:var(--white);font-size:11px;font-weight:700}
.contact-row{display:flex;gap:18px;font-size:12.5px;line-height:20px;margin-bottom:18px}
.contact-row svg{flex:none;margin-top:3px}
.footer-bottom{position:absolute;left:98px;right:100px;top:312px;border-top:1px solid #3a3a3a}
.copyright{position:absolute;left:0;top:22px;font-size:12px}
.social{position:absolute;right:0;top:14px;display:flex;gap:10px}
.social span{width:30px;height:30px;border-radius:50%;border:1px solid #777}
</style>
</head>
<body>

<header class="site-header">
  <div class="topbar">
    <span><svg width="14" height="14" viewBox="0 0 24 24"><path fill="#c8161d" d="M6.6 10.8a15 15 0 0 0 6.6 6.6l2.2-2.2c.3-.3.7-.4 1-.2 1.1.4 2.3.6 3.6.6.6 0 1 .4 1 1V20c0 .6-.4 1-1 1A17 17 0 0 1 3 4c0-.6.4-1 1-1h3.5c.6 0 1 .4 1 1 0 1.3.2 2.5.6 3.6.1.3 0 .7-.2 1z"/></svg>555 210 4477</span>
    <span class="sep">|</span>
    <span><svg width="15" height="12" viewBox="0 0 24 18"><rect x="1" y="1" width="22" height="16" rx="1" fill="#c8161d"/><path d="M1 1l11 9 11-9" stroke="#fff" stroke-width="2" fill="none"/></svg>hello@blueharbor-sec.com</span>
  </div>
  <nav class="main-nav">
    <span class="active">HOME</span><span>ABOUT US</span><span>SERVICES</span><span>NEWS</span><span>CONTACT US</span>
    <svg width="15" height="15" viewBox="0 0 24 24"><circle cx="10" cy="10" r="7" stroke="#2b2b2b" stroke-width="3" fill="none"/><path d="M15 15l7 7" stroke="#2b2b2b" stroke-width="3"/></svg>
  </nav>
</header>
<div class="brand-disc"></div>
<div class="brand"><div class="mark"></div><div class="name">BLUE HARBOR</div></div>

<section class="hero" role="img" aria-label="Hands touching a glowing penetration test security interface">
  <div class="tagline-small">Offensive Services from</div>
  <div class="tagline-big">OFFENSIVE MINDS</div>
  <div class="dots"><span class="on"></span><span></span><span></span><span></span></div>
</section>

<h2 class="section-title" style="top:632px">WELCOME TO BLUE HARBOR</h2>
<p class="welcome-text">We do security consulting, specifically offensive security. The technical term is "Penetration Testing", but you probably know it as "hacking". Companies hire us to break in before the bad guys do.</p>

<div class="feature" style="left:100px">
  <svg width="84" height="84" viewBox="0 0 84 84"><circle cx="42" cy="42" r="32" stroke="#2b2b2b" stroke-width="2" fill="none"/><circle cx="42" cy="42" r="22" fill="#c8161d"/><rect x="33" y="40" width="18" height="13" rx="2" fill="#fff"/><path d="M36 40v-5a6 6 0 0 1 12 0v5" stroke="#fff" stroke-width="2.5" fill="none"/><circle cx="42" cy="6" r="5" fill="#c8161d"/><circle cx="42" cy="78" r="5" fill="#c8161d"/><circle cx="6" cy="42" r="5" fill="#c8161d"/><circle cx="78" cy="42" r="5" fill="#c8161d"/></svg>
  <h3>Security Consulting</h3>
  <p>At vero eos et accusamus et iusto odio dignissimos ducimus qui blanditis praesen tium voluptatum deleniti aocca</p>
</div>
<div class="feature" style="left:435px">
  <svg width="84" height="84" viewBox="0 0 84 84"><path d="M22 8h28l14 14v50H22z" stroke="#2b2b2b" stroke-width="4" fill="none" stroke-linejoin="round"/><path d="M50 8v14h14" stroke="#2b2b2b" stroke-width="4" fill="none"/><rect x="44" y="52" width="26" height="22" rx="2" fill="#c8161d"/><path d="M49 52v-6a8 8 0 0 1 16 0v6" stroke="#c8161d" stroke-width="4" fill="none"/></svg>
  <h3>Offensive Security</h3>
  <p>At vero eos et accusamus et iusto odio dignissimos ducimus qui blanditis praesen tium voluptatum deleniti aocca</p>
</div>
<div class="feature" style="left:770px">
  <svg width="84" height="84" viewBox="0 0 84 84"><rect x="6" y="12" width="26" height="36" fill="#c8161d"/><path d="M10 20h18M10 27h18M10 34h18M10 41h12" stroke="#fff" stroke-width="2"/><rect x="24" y="18" width="54" height="40" stroke="#2b2b2b" stroke-width="4" fill="#fff"/><path d="M32 28h38M32 36h38M32 44h26" stroke="#2b2b2b" stroke-width="3"/><path d="M44 58v10h14V58M36 72h30" stroke="#2b2b2b" stroke-width="4"/></svg>
  <h3>Penetration Testing</h3>
  <p>At vero eos et accusamus et iusto odio dignissimos ducimus qui blanditis praesen tium voluptatum deleniti aocca</p>
</div>

<section class="video-band" role="img" aria-label="Video still of hands typing on a laptop">
  <div class="play"><svg width="62" height="62" viewBox="0 0 62 62"><path d="M25 19l18 12-18 12z" fill="#fff"/></svg></div>
</section>

<h2 class="section-title" style="top:1540px">OUR SERVICES</h2>
<div class="service" style="left:98px;top:1630px;width:497px;height:210px"><div class="photo" role="img" aria-label="Team working at monitors in a dark operations room" style="background:linear-gradient(135deg,#1d2a38,#3e5670)"></div><div class="label">Red Team Adversary Simulation</div></div>
<div class="service" style="left:605px;top:1630px;width:242px;height:210px"><div class="photo" role="img" aria-label="Colleagues reviewing documents at a desk" style="background:linear-gradient(135deg,#b9b6b2,#6f6a66)"></div><div class="label">Internal Pivot Assessment &amp; Post Exploitation</div></div>
<div class="service" style="left:858px;top:1630px;width:244px;height:210px"><div class="photo" role="img" aria-label="Engineer testing electronic hardware" style="background:linear-gradient(135deg,#8a7a6c,#4a3d34)"></div><div class="label">Advanced Product, Hardware &amp; RF Testing</div></div>
<div class="service" style="left:98px;top:1853px;width:244px;height:210px"><div class="photo" role="img" aria-label="Hands holding a smartphone" style="background:linear-gradient(135deg,#8f9498,#4c5257)"></div><div class="label">Mobile Application Assessment</div></div>
<div class="service" style="left:352px;top:1853px;width:243px;height:210px"><div class="photo" role="img" aria-label="Analyst working at a computer at night" style="background:linear-gradient(135deg,#4a3a2f,#1f1a17)"></div><div class="label">External Penetration Testing</div></div>
<div class="service" style="left:605px;top:1853px;width:242px;height:210px"><div class="photo" role="img" aria-label="Magnifying glass over a keyboard" style="background:linear-gradient(135deg,#5d6166,#2a2d31)"></div><div class="label">Internal Penetration Testing</div></div>
<div class="service" style="left:858px;top:1853px;width:244px;height:210px"><div class="photo" role="img" aria-label="Hands typing on a laptop in warm light" style="background:linear-gradient(135deg,#c98a5a,#6a3e2a)"></div><div class="label">Web Application Penetration Testing</div></div>

<section class="testimonials">
  <h2 class="section-title">CLIENT TESTIMONIALS</h2>
  <div class="arrow" style="left:30px"><svg width="32" height="32" viewBox="0 0 32 32"><path d="M18 10l-6 6 6 6" stroke="#fff" stroke-width="2" fill="none"/></svg></div>
  <div class="arrow" style="right:30px"><svg width="32" height="32" viewBox="0 0 32 32"><path d="M14 10l6 6-6 6" stroke="#fff" stroke-width="2" fill="none"/></svg></div>
  <div class="quote-card" style="left:98px">
    <div class="avatar" role="img" aria-label="Client portrait"></div>
    <div class="body">
      <div class="q"><b>“</b>At vero eos et accusamus et iustodio dignissimos ducimus qui blanditiispraesent ium voluptatum deleniti atqu.</div>
      <div class="who">Laura Benton</div>
      <div class="role">Financial Services Professional</div>
      <div class="stars">★★★★☆</div>
    </div>
  </div>
  <div class="quote-card" style="left:442px">
    <div class="avatar" role="img" aria-label="Client portrait"></div>
    <div class="body">
      <div class="q"><b>“</b>At vero eos et accusamus et iustodio dignissimos ducimus qui blanditiispraesent ium voluptatum deleniti atqu.</div>
      <div class="who">Marisol T. Vega</div>
      <div class="role">Regional Policy Fellow at the Institute</div>
      <div class="stars">★★★★½</div>
    </div>
  </div>
  <div class="quote-card" style="left:791px">
    <div class="avatar" role="img" aria-label="Client portrait"></div>
    <div class="body">
      <div class="q"><b>“</b>At vero eos et accusamus et iustodio dignissimos ducimus qui blanditiispraesent ium voluptatum deleniti atqu.</div>
      <div class="who">Ruth Calder</div>
      <div class="role">Creative Strategist | Entrepreneur &amp; Founder</div>
      <div class="stars">★★★★☆</div>
    </div>
  </div>
</section>

<h2 class="section-title" style="top:2590px">LATEST NEWS</h2>
<article class="news" style="left:98px">
  <div class="photo" role="img" aria-label="Support operator wearing a headset" style="background:linear-gradient(135deg,#5d6f82,#2a3440)"></div>
  <h3>Finibus Bonorumet Maloru</h3>
  <div class="meta">▦ 25/09/2017 <span class="bar"></span> ◉ Mark</div>
  <p>Neque porro quisquam est, qui dolorem ipsqu ia dolor sit amet, consectetur, adipisci</p>
  <div class="more">READ MORE</div>
</article>
<article class="news" style="left:437px">
  <div class="photo" role="img" aria-label="Server racks in a data centre" style="background:linear-gradient(135deg,#1f3a4a,#4aa0a8)"></div>
  <h3>Finibus Bonorumet Maloru</h3>
  <div class="meta">▦ 25/09/2017 <span class="bar"></span> ◉ Mark</div>
  <p>Neque porro quisquam est, qui dolorem ipsqu ia dolor sit amet, consectetur, adipisci</p>
  <div class="more">READ MORE</div>
</article>
<article class="news" style="left:777px">
  <div class="photo" role="img" aria-label="Phone showing a security lock beside a laptop" style="background:linear-gradient(135deg,#dfe3e8,#7f8ea0)"></div>
  <h3>Finibus Bonorumet Maloru</h3>
  <div class="meta">▦ 25/09/2017 <span class="bar"></span> ◉ Mark</div>
  <p>Neque porro quisquam est, qui dolorem ipsqu ia dolor sit amet, consectetur, adipisci</p>
  <div class="more">READ MORE</div>
</article>

<footer class="site-footer">
  <div class="footer-brand"><div class="mark"></div><div class="name">BLUE HARBOR</div></div>
  <div class="footer-col" style="left:384px">
    <h4>Quick Links</h4>
    <ul><li>Home</li><li>About us</li><li>Services</li><li>News</li><li>Contact Us</li></ul>
  </div>
  <div class="footer-col" style="left:551px;width:270px">
    <h4>Newsletter Subscription</h4>
    <p>Register your Email Address to get information about us</p>
    <div class="news-input"></div>
    <span class="subscribe">SUBSCRIBE</span>
  </div>
  <div class="footer-col" style="left:884px;width:220px">
    <h4>Contact Us</h4>
    <div class="contact-row"><svg width="12" height="16" viewBox="0 0 12 16"><path d="M6 0a6 6 0 0 0-6 6c0 4.5 6 10 6 10s6-5.5 6-10a6 6 0 0 0-6-6zm0 8.5A2.5 2.5 0 1 1 6 3.5a2.5 2.5 0 0 1 0 5z" fill="#fff"/></svg><span>Harbor Lane 14, Floor 3, Suite 6, Dockside 20145, Portvale</span></div>
    <div class="contact-row"><svg width="13" height="13" viewBox="0 0 24 24"><path fill="#fff" d="M6.6 10.8a15 15 0 0 0 6.6 6.6l2.2-2.2c.3-.3.7-.4 1-.2 1.1.4 2.3.6 3.6.6.6 0 1 .4 1 1V20c0 .6-.4 1-1 1A17 17 0 0 1 3 4c0-.6.4-1 1-1h3.5c.6 0 1 .4 1 1 0 1.3.2 2.5.6 3.6.1.3 0 .7-.2 1z"/></svg><span>555 210 4477</span></div>
    <div class="contact-row"><svg width="14" height="11" viewBox="0 0 24 18"><rect x="1" y="1" width="22" height="16" fill="#fff"/><path d="M1 1l11 9 11-9" stroke="#232323" stroke-width="2" fill="none"/></svg><span>hello@blueharbor-sec.com</span></div>
  </div>
  <div class="footer-bottom">
    <div class="copyright">Copyrights © 2017, Blue Harbor. All rights reserved.</div>
    <div class="social"><span></span><span></span><span></span><span></span></div>
  </div>
</footer>

</body>
</html>
```